The Bright Path Foundation

This is a non profit . We are a 501(c)(3) charitable organization in the United States. The organization is a volunteer based group providing basic healthcare to those living in underserved rural areas around the world. I have attached a brochure that provides some information about the organization. We are looking for a basic 5 page web page Page 1 Photos that fade into the next x 3 with mission statementPage 2 About us - details about bright path foundation. also introducing our Founders of the organization. Marlene Quist, M.D. Doria Lemke , FNP, Paula Dweck, FNP, Brent Lomax. ( will provide you info on each.Page 3 Projects coming up and futurePage 4 Get involved - Give a donation, Volunteer, Corporate supportPage 5 Support us and contact us with a message box.We mainly work in South America but anticipate trave to South Africa in the near future. Colors bright with emphasis on Reds and Purples. I have attached some photos and ideas. You can use or not use ok to use something similar if you so like

Target Market(s)

People interested in volunteering time or money to overseas medical work. NOT a religious base

Colors
876aae
ec1f27
f37022
9bcb3c

Requirements
Must have
• Colorful pictures nature, brings out emotion, colorful, children from various parts of the world, animals.
• Tried to down load some pictures but would not go thru.

```html
<!DOCTYPE html>
<html lang="en">
<head>
<meta charset="utf-8">
<title>The Bright Path Foundation</title>
<link rel="stylesheet" href="https://fonts.googleapis.com/css2?family=Merriweather+Sans:wght@400;600;700&family=Merriweather:wght@400;700&display=swap">
<style>
:root{
  --purple:#8a63c9;
  --purple-deep:#7a55b8;
  --purple-light:#a682dc;
  --purple-text:#7d5bb5;
  --green:#8dc63f;
  --green-dark:#79ad33;
  --ink:#2b2838;
  --muted:#6b6778;
  --white:#ffffff;
  --line:#e7e3ee;
}
*{box-sizing:border-box;margin:0;padding:0}
html,body{width:1200px;height:4494px;overflow:hidden}
body{position:relative;background:var(--white);font-family:"Merriweather",Georgia,serif;color:var(--ink)}
.abs{position:absolute}
.sans{font-family:"Merriweather Sans",Arial,sans-serif}
.eyebrow{font-family:"Merriweather Sans",Arial,sans-serif;font-size:11px;font-weight:600;color:var(--green);letter-spacing:.5px;text-transform:uppercase}
.heading{font-family:"Merriweather Sans",Arial,sans-serif;font-weight:600;font-size:26px;line-height:40px;color:var(--ink)}
.heading em{font-style:normal;color:var(--purple-text)}
.body-text{font-size:12px;line-height:20px;color:var(--muted)}
.btn{position:absolute;display:flex;align-items:center;justify-content:center;font-family:"Merriweather Sans",Arial,sans-serif;font-size:11px;font-weight:600;letter-spacing:.6px;color:var(--white);background:var(--green);text-transform:uppercase}
.btn.ghost{background:transparent;border:2px solid var(--white)}
.photo{position:absolute}
/* hero */
.hero{position:absolute;left:0;top:0;width:1200px;height:676px;background:linear-gradient(135deg,#9a74d6 0%,#8a63c9 60%,#9470d2 100%)}
.hero-wash{position:absolute;left:200px;top:0;width:560px;height:676px;background:linear-gradient(90deg,rgba(255,255,255,0),rgba(190,120,210,.25),rgba(255,255,255,0))}
.logo-box{position:absolute;left:89px;top:0;width:158px;height:77px;background:var(--white);border-radius:0 0 14px 14px;display:flex;align-items:center;justify-content:center;gap:6px}
.logo-box span{font-family:"Merriweather Sans",Arial,sans-serif;font-size:12px;font-weight:600;color:var(--purple-text)}
.logo-dot{width:10px;height:10px;border-radius:50%;background:var(--purple)}
.nav{position:absolute;top:30px;left:0;width:1200px;font-family:"Merriweather Sans",Arial,sans-serif;font-size:11px;color:var(--white)}
.nav a{position:absolute;color:var(--white);text-decoration:none}
.nav .active{font-weight:700}
.nav .active::after{content:"";position:absolute;left:0;right:0;top:22px;height:2px;background:var(--white)}
.hero-title{left:89px;top:272px;font-family:"Merriweather Sans",Arial,sans-serif;font-weight:600;font-size:36px;color:var(--white)}
.hero-sub{left:89px;top:326px;width:520px;font-size:12px;line-height:20px;color:#e7dcf6}
.dots{left:553px;top:623px;display:flex;gap:12px}
.dots i{display:block;width:20px;height:3px;background:rgba(255,255,255,.5)}
.dots i:first-child{background:var(--white)}
/* sections */
.divider{position:absolute;left:428px;width:344px;height:2px;background:var(--purple)}
.stat{position:absolute;top:1780px}
.stat b{display:block;font-family:"Merriweather Sans",Arial,sans-serif;font-size:40px;font-weight:600;color:var(--purple-text)}
.stat span{display:block;margin-top:10px;font-size:12px;color:var(--muted)}
.founders{position:absolute;left:0;top:2027px;width:1200px;height:671px;background:linear-gradient(180deg,#8a63c9,#a07ddb)}
.founder-card{position:absolute;top:2295px;height:280px;border-radius:8px;overflow:hidden}
.founder-name{position:absolute;left:20px;top:210px;font-family:"Merriweather Sans",Arial,sans-serif;font-size:17px;font-weight:700;color:var(--white)}
.founder-role{position:absolute;left:20px;top:242px;font-size:10px;color:var(--white)}
.arrow-next{position:absolute;left:1150px;top:2387px;width:56px;height:56px;border-radius:50%;background:var(--white);box-shadow:0 2px 8px rgba(0,0,0,.2)}
.project-card{position:absolute;top:2920px;width:336px;height:382px;background:var(--white);box-shadow:0 2px 14px rgba(0,0,0,.1);border-radius:4px;overflow:hidden}
.project-card .photo{left:0;top:0;width:336px;height:175px}
.project-card .bar{position:absolute;left:0;top:175px;width:336px;height:6px;background:var(--green)}
.project-card .pct{position:absolute;right:14px;top:160px;width:36px;height:36px;border-radius:50%;background:var(--green);color:var(--white);font-family:"Merriweather Sans",Arial,sans-serif;font-size:9px;font-weight:700;display:flex;align-items:center;justify-content:center}
.project-card .cat{position:absolute;left:14px;top:214px;font-size:8px}
.project-card .title{position:absolute;left:14px;top:236px;font-family:"Merriweather Sans",Arial,sans-serif;font-size:15px;font-weight:700;color:var(--ink)}
.project-card .money{position:absolute;top:305px;font-family:"Merriweather Sans",Arial,sans-serif;font-size:18px;color:var(--purple-text);font-weight:600}
.project-card .money small{display:block;font-family:"Merriweather",Georgia,serif;font-size:9px;color:var(--muted);font-weight:400;margin-top:4px}
.project-card .btn{left:232px;top:310px;width:86px;height:32px;font-size:9px}
.donate-panel{position:absolute;left:0;top:3374px;width:600px;height:339px;background:linear-gradient(135deg,#8a63c9,#9d78d8)}
.corporate-panel{position:absolute;left:600px;top:3374px;width:600px;height:339px;background:#fbfafd}
.panel-title{position:absolute;font-family:"Merriweather Sans",Arial,sans-serif;font-size:32px;font-weight:600}
.volunteer-panel{position:absolute;left:600px;top:3713px;width:600px;height:336px;background:var(--green)}
.field{position:absolute;height:46px;background:rgba(255,255,255,.22);font-size:11px;color:var(--white);padding:14px 12px}
.footer-label{font-family:"Merriweather Sans",Arial,sans-serif;font-size:12px;font-weight:700;color:var(--ink)}
.contact-row{position:absolute;left:439px;font-size:10px;color:var(--ink);display:flex}
.contact-row b{width:72px;font-family:"Merriweather Sans",Arial,sans-serif;font-weight:700}
.social{position:absolute;top:4220px;width:46px;height:46px;border-radius:50%;background:var(--purple)}
</style>
</head>
<body>

<!-- HERO -->
<section class="hero">
  <div class="hero-wash"></div>
  <div class="logo-box"><i class="logo-dot"></i><span>Bright Path Foundation</span></div>
  <nav class="nav">
    <a class="active" style="left:632px">Home</a>
    <a style="left:706px">Our Mission</a>
    <a style="left:813px">About Us</a>
    <a style="left:905px">Projects</a>
    <a style="left:989px">Support</a>
    <a style="left:1073px">Contact</a>
  </nav>
  <h1 class="abs hero-title">Helping Humanity.</h1>
  <p class="abs hero-sub">Caring hands bring basic health to rural villages, one family and one clinic day at a time.</p>
  <div class="btn" style="left:89px;top:420px;width:161px;height:40px">Donate Now</div>
  <div class="btn ghost" style="left:260px;top:420px;width:161px;height:40px">Learn More</div>

  <svg class="photo" style="left:683px;top:128px" width="187" height="158" viewBox="0 0 187 158" role="img" aria-label="Photo of smiling children outdoors">
    <path d="M30 10 C90 -10 170 10 182 60 C192 110 150 150 95 152 C40 155 5 120 4 80 C2 45 10 18 30 10Z" fill="#b89a7a" stroke="var(--green)" stroke-width="4"/>
  </svg>
  <svg class="photo" style="left:686px;top:228px" width="502" height="374" viewBox="0 0 502 374" role="img" aria-label="Photo of a volunteer caring for children">
    <defs><linearGradient id="heroG" x1="0" y1="0" x2="1" y2="1"><stop offset="0" stop-color="#5a4a45"/><stop offset=".5" stop-color="#c9b7a6"/><stop offset="1" stop-color="#3f8cc9"/></linearGradient></defs>
    <path d="M60 90 C130 10 260 60 330 20 C420 -20 500 60 492 170 C485 280 420 360 300 366 C170 372 40 340 12 250 C-10 180 20 130 60 90Z" fill="url(#heroG)" stroke="var(--green)" stroke-width="6"/>
  </svg>
  <svg class="photo" style="left:1045px;top:535px" width="107" height="85" viewBox="0 0 107 85" role="img" aria-label="Photo of hands reaching out">
    <path d="M20 8 C60 -4 104 10 102 45 C100 78 60 84 30 78 C6 72 0 40 20 8Z" fill="#d8cbbd" stroke="var(--white)" stroke-width="4"/>
  </svg>
  <div class="abs dots"><i></i><i></i><i></i></div>
</section>

<!-- MISSION -->
<svg class="photo" style="left:0;top:727px" width="500" height="548" viewBox="0 0 500 548" role="img" aria-label="Photo of a young child standing in a green field">
  <defs><linearGradient id="missionG" x1="0" y1="0" x2="1" y2="1"><stop offset="0" stop-color="#3f5a2c"/><stop offset=".55" stop-color="#6f8a4a"/><stop offset="1" stop-color="#b06a55"/></linearGradient></defs>
  <path d="M0 0 C140 -10 300 40 420 60 C500 80 520 180 470 300 C420 430 300 520 150 540 C70 550 20 530 0 520 Z" fill="url(#missionG)" stroke="var(--purple)" stroke-width="5"/>
</svg>
<p class="abs eyebrow" style="left:604px;top:858px">Our Mission</p>
<h2 class="abs heading" style="left:604px;top:880px;width:480px">We are helping <em>120,000 families and people</em> around the globe</h2>
<p class="abs body-text" style="left:604px;top:976px;width:430px">Clinic teams travel to remote villages with medicine, checkups and care. Local partners help us reach the people most in need.</p>
<p class="abs body-text" style="left:604px;top:1052px;width:430px">Every visit trains local helpers so good health can last long after the team goes home.</p>
<div class="btn" style="left:604px;top:1128px;width:163px;height:40px">Know More</div>
<div class="divider" style="top:1348px"></div>

<!-- ABOUT -->
<p class="abs eyebrow" style="left:89px;top:1512px">About Us</p>
<h2 class="abs heading" style="left:89px;top:1534px;width:520px">Founded in <em>1996</em>, We are operating in <em>120 Underserved Areas</em></h2>
<p class="abs body-text" style="left:89px;top:1634px;width:420px">Our volunteers give their time and skill to bring basic healthcare to rural towns. Nurses, doctors and helpers work side by side with local leaders. Each year we open new clinic days and bring supplies where roads end.</p>
<div class="stat" style="left:89px"><b>983</b><span>Volunteers</span></div>
<div class="stat" style="left:260px"><b>230</b><span>Families Helped</span></div>
<div class="stat" style="left:433px"><b>10</b><span>Awards</span></div>
<svg class="photo" style="left:696px;top:1420px" width="492" height="532" viewBox="0 0 492 532" role="img" aria-label="Collage of photos of children and families from around the world">
  <defs><linearGradient id="aboutG" x1="0" y1="0" x2="1" y2="1"><stop offset="0" stop-color="#8a4a3a"/><stop offset=".5" stop-color="#6a5248"/><stop offset="1" stop-color="#b9b3ad"/></linearGradient></defs>
  <path d="M60 20 C150 -10 300 0 420 30 C490 50 495 150 470 260 C440 400 380 500 260 525 C150 545 80 470 50 360 C20 250 -10 60 60 20Z" fill="url(#aboutG)" stroke="var(--green)" stroke-width="6"/>
</svg>

<!-- FOUNDERS -->
<section class="founders"></section>
<h2 class="abs sans" style="left:89px;top:2148px;font-size:24px;font-weight:600;color:var(--white)">Our Founders</h2>
<p class="abs body-text" style="left:89px;top:2204px;width:620px;color:#eee6fa">Meet the team who started it all, caring people with years of field work in rural clinics and a shared dream of health for all.</p>
<div class="founder-card" style="left:89px;width:281px;background:linear-gradient(180deg,#6a4a3a,#2a1e22)" role="img" aria-label="Portrait photo of founder Doria Lemke">
  <div class="founder-name">DORIA LEMKE</div>
  <div class="founder-role">FNP</div>
</div>
<div class="founder-card" style="left:377px;width:281px;background:linear-gradient(135deg,#6a3fc0,#c050d0)" role="img" aria-label="Portrait photo of founder Brent Lomax"></div>
<div class="founder-card" style="left:668px;width:281px;background:linear-gradient(135deg,#7d8a70,#3c3a3a)" role="img" aria-label="Portrait photo of founder Paula Dweck"></div>
<div class="founder-card" style="left:956px;width:260px;border-radius:8px 0 0 8px;background:linear-gradient(135deg,#c9a27a,#8a7058)" role="img" aria-label="Portrait photo of founder Marlene Quist"></div>
<div class="arrow-next"><svg width="56" height="56" viewBox="0 0 56 56"><path d="M24 20 L32 28 L24 36" fill="none" stroke="var(--ink)" stroke-width="2.5"/></svg></div>

<!-- PROJECTS -->
<p class="abs eyebrow" style="left:87px;top:2777px;font-size:9px">Our Projects</p>
<h2 class="abs heading" style="left:87px;top:2800px;width:520px;font-size:22px;line-height:38px">We believe to <em>grow community</em> in order to help a <em>noble cause</em></h2>
<div class="btn" style="left:946px;top:2818px;width:163px;height:40px">View All</div>

<article class="project-card" style="left:87px">
  <div class="photo" style="background:linear-gradient(135deg,#5a4a40,#a07e68)" role="img" aria-label="Photo of a large crowd at a medical camp"></div>
  <div class="bar"></div><div class="pct">80%</div>
  <p class="cat eyebrow">Disaster Management</p>
  <h3 class="title">Cuba Medical Camp - 2019</h3>
  <div class="money" style="left:14px">$500<small>Goal</small></div>
  <div class="money" style="left:86px">$398<small>Pledged</small></div>
  <div class="btn">Donate</div>
</article>
<article class="project-card" style="left:434px">
  <div class="photo" style="background:linear-gradient(135deg,#8a7a58,#c9b38a)" role="img" aria-label="Photo of a child walking on a dirt road"></div>
  <div class="bar"></div><div class="pct">58%</div>
  <p class="cat eyebrow">Places</p>
  <h3 class="title">Food &amp; Med Collection</h3>
  <div class="money" style="left:14px">$983<small>Goal</small></div>
  <div class="money" style="left:86px">$568<small>Pledged</small></div>
  <div class="btn">Donate</div>
</article>
<article class="project-card" style="left:778px">
  <div class="photo" style="background:linear-gradient(135deg,#4a4a4a,#b04040)" role="img" aria-label="Photo of a red supply kit on a rocky shore"></div>
  <div class="bar"></div><div class="pct">67%</div>
  <p class="cat eyebrow">Diseases</p>
  <h3 class="title">AIDS Medical Checkup</h3>
  <div class="money" style="left:14px">$780<small>Goal</small></div>
  <div class="money" style="left:86px">$700<small>Pledged</small></div>
  <div class="btn">Donate</div>
</article>

<!-- GET INVOLVED -->
<section class="donate-panel"></section>
<section class="corporate-panel"></section>
<p class="abs sans" style="left:89px;top:3462px;font-size:13px;color:var(--white);letter-spacing:.5px">DONATIONS</p>
<h2 class="panel-title" style="left:89px;top:3494px;color:var(--white)">Become Our <span style="color:var(--green)">Donor</span></h2>
<div class="btn" style="left:89px;top:3585px;width:163px;height:40px">Know More</div>
<p class="abs sans" style="left:645px;top:3462px;font-size:13px;color:var(--green);letter-spacing:.5px">SPONSORING</p>
<h2 class="panel-title" style="left:645px;top:3494px;color:var(--ink)">Become Our <span style="color:var(--purple-text)">Corporate</span></h2>
<div class="btn" style="left:645px;top:3585px;width:163px;height:40px">Know More</div>

<div class="photo" style="left:0;top:3713px;width:600px;height:336px;background:linear-gradient(135deg,#2f9fc9,#6aa060 60%,#d0453f)" role="img" aria-label="Photo of smiling volunteers holding a red paper heart"></div>
<section class="volunteer-panel"></section>
<h2 class="panel-title" style="left:645px;top:3754px;color:var(--white)">Become Our Volunteer</h2>
<div class="field" style="left:645px;top:3830px;width:209px">First Name</div>
<div class="field" style="left:862px;top:3830px;width:250px">Last Name</div>
<div class="field" style="left:645px;top:3886px;width:467px">Address</div>
<p class="abs" style="left:645px;top:3976px;font-size:9px;color:var(--white)">Your information will be secured &amp; confidential</p>
<div class="btn ghost" style="left:951px;top:3960px;width:161px;height:44px">Join Us</div>

<!-- FOOTER -->
<div class="abs" style="left:94px;top:4210px;display:flex;align-items:center;gap:10px">
  <i class="logo-dot" style="width:16px;height:16px"></i>
  <span class="sans" style="font-size:20px;font-weight:600;color:var(--purple-text)">Bright Path Foundation</span>
</div>
<p class="abs footer-label" style="left:439px;top:4174px">CONTACT INFO</p>
<div class="contact-row" style="top:4214px"><b>Address:</b><span>418 Orchard Lane,<br>Dayton, OH 45402</span></div>
<div class="contact-row" style="top:4256px"><b>Phone:</b><span>(555) 204-3187</span></div>
<div class="contact-row" style="top:4286px"><b>Email:</b><span>hello@brightpathmail.org</span></div>
<p class="abs footer-label" style="left:870px;top:4174px">PRODUCT TAGS</p>
<i class="social" style="left:868px"></i>
<i class="social" style="left:932px"></i>
<i class="social" style="left:995px"></i>
<svg class="abs" style="left:1112px;top:4353px" width="56" height="56" viewBox="0 0 56 56" aria-hidden="true">
  <circle cx="28" cy="28" r="28" fill="var(--purple)"/>
  <path d="M18 20 H38 V33 H27 L21 38 V33 H18 Z" fill="var(--white)"/>
</svg>
<div class="divider" style="top:4421px"></div>
<p class="abs sans" style="left:0;top:4455px;width:1200px;text-align:center;font-size:9px;font-weight:600;color:var(--ink)">© BRIGHT PATH FOUNDATION. 2019. All Rights Reserved</p>

</body>
</html>
```